Rebrand of an existing product label

We are looking for a new design / label for our body lotion. Attached is the current product label. We have this product available in Retinol, Collagen, Hyaluronic Acid, Vitamin C, and Coconut. The brand should reflect a clinical, trustworthy look. We also want to include on the label that the product contains Dead Sea Minerals. Attached is the dieline for the label for the jar and the top. This jar is the packaging that needs to be used for this project.
Updates

Target Market(s)

40+

Requirements
Must have
• Ingredient callouts on the front + benefits. Ex- Vitamin C Brightening Cream

```html
<!DOCTYPE html>
<html lang="en">
<head>
<meta charset="UTF-8">
<title>Body Lotion – Jar and Lid Labels</title>
<link rel="stylesheet" href="https://fonts.googleapis.com/css2?family=Archivo+Black&family=Jost:wght@400;500&family=Oswald:wght@600&family=Poppins:wght@600&family=Open+Sans:wght@500;600&display=swap">
<style>
  :root {
    --bg: #f6e6ea;
    --label-base: #efe6ee;
    --label-light: #f8f4f7;
    --lilac: #ddd0e2;
    --pink: #d05aa3;
    --pink-bar: #c8589e;
    --ink: #2a2a2a;
    --brand-ink: #2f3a36;
    --white: #ffffff;
  }
  * { margin: 0; padding: 0; box-sizing: border-box; }
  html, body { width: 1200px; height: 900px; overflow: hidden; background: var(--bg); }
  .canvas { position: relative; width: 1200px; height: 900px; }

  /* Lid label */
  .lid-label {
    position: absolute; left: 380px; top: 40px; width: 440px; height: 230px;
    border-radius: 50%;
    background: linear-gradient(160deg, var(--label-light) 0%, var(--label-base) 60%, var(--lilac) 100%);
    overflow: hidden;
  }
  .lid-label .lid-floral {
    position: absolute; right: 40px; top: 40px; width: 160px; height: 150px;
    border-radius: 50%;
    background: radial-gradient(circle, rgba(183,170,210,.55), rgba(221,208,226,0));
  }
  .lid-title {
    position: absolute; left: 0; right: 0; top: 88px; text-align: center;
    font-family: "Archivo Black", sans-serif; font-size: 34px; letter-spacing: 2px;
    color: var(--pink);
  }
  .lid-subtitle {
    position: absolute; left: 0; right: 0; top: 132px; text-align: center;
    font-family: "Archivo Black", sans-serif; font-size: 11px; letter-spacing: 1px; line-height: 1.05;
    color: var(--ink);
  }

  /* Jar wrap label */
  .jar-label {
    position: absolute; left: 150px; top: 300px; width: 900px; height: 560px;
    background: linear-gradient(180deg, var(--label-base) 0%, var(--label-light) 70%, var(--label-base) 100%);
    overflow: hidden;
  }
  .jar-label .floral-left {
    position: absolute; left: 30px; top: 60px; width: 200px; height: 320px;
    border-radius: 45%;
    background: radial-gradient(ellipse, rgba(183,170,210,.5), rgba(221,208,226,0) 70%);
  }
  .jar-label .floral-right {
    position: absolute; right: 30px; top: 180px; width: 200px; height: 320px;
    border-radius: 45%;
    background: radial-gradient(ellipse, rgba(183,170,210,.45), rgba(221,208,226,0) 70%);
  }
  .brand-tab {
    position: absolute; left: 290px; top: 0; width: 320px; height: 150px;
    background: var(--label-light); border-radius: 0 0 36px 36px;
    display: flex; align-items: center; justify-content: center; gap: 14px;
  }
  .brand-dot { width: 14px; height: 14px; border-radius: 50%; background: var(--brand-ink); }
  .brand-name {
    font-family: "Jost", sans-serif; font-weight: 400; font-size: 40px;
    letter-spacing: 1px; color: var(--brand-ink);
  }
  .bar {
    position: absolute; left: 140px; width: 620px; height: 30px;
    background: var(--pink-bar); border-radius: 15px;
    display: flex; align-items: center; justify-content: center;
    font-family: "Open Sans", sans-serif; font-weight: 500; color: var(--white);
  }
  .bar-size { top: 178px; font-size: 18px; letter-spacing: 12px; }
  .bar-minerals { top: 430px; font-size: 15px; letter-spacing: 3px; }
  .uses {
    position: absolute; left: 0; right: 0; top: 222px; text-align: center;
    font-family: "Poppins", sans-serif; font-weight: 600; font-size: 40px; color: var(--ink);
  }
  .product-name {
    position: absolute; left: 0; right: 0; top: 290px; text-align: center;
    font-family: "Oswald", sans-serif; font-weight: 600; font-size: 96px; line-height: 1.1;
    color: var(--pink);
  }
  .variant-line {
    position: absolute; left: 0; right: 0; top: 486px; text-align: center;
    font-family: "Open Sans", sans-serif; font-weight: 600; font-size: 22px; letter-spacing: 6px;
    color: var(--ink);
  }
  .variant-line .divider { display: inline-block; width: 2px; height: 24px; background: var(--ink); vertical-align: middle; margin: 0 8px; }
</style>
</head>
<body>
<main class="canvas">
  <section class="lid-label">
    <div class="lid-floral" role="img" aria-label="Soft lilac leaf and flower illustration"></div>
    <h2 class="lid-title">BODY LOTION</h2>
    <p class="lid-subtitle">MOISTURIZING FACE, NECK<br>&amp; HANDS</p>
  </section>

  <section class="jar-label">
    <div class="floral-left" role="img" aria-label="Soft lilac leaf and berry sprig illustration"></div>
    <div class="floral-right" role="img" aria-label="Soft lilac leaf and flower illustration"></div>

    <div class="brand-tab">
      <span class="brand-dot"></span>
      <span class="brand-name">LUMERA SKIN</span>
    </div>

    <div class="bar bar-size">PROFESSIONAL SIZE</div>
    <p class="uses">MOISTURIZING FACE, NECK &amp; HANDS</p>
    <h1 class="product-name">BODY LOTION</h1>
    <div class="bar bar-minerals">CONTAIN DEAD SEA MINERALS</div>
    <p class="variant-line">VITAMIN C BRIGHTENING CREAM<span class="divider"></span>16.9 FL OZ (500 ML)</p>
  </section>
</main>
</body>
</html>
```